businesscard, flyer and membercard

--------------------------------------------------------------------------------------------------
design flyer :
- delivering format (jpg, pdf and original psd)
- there is a example how the flyers should look like
the text and logo should be the same as the exemple flyer, the creativity is yours.
- the design should have a back and front side.
File format : 15,0 cm x 21,2 cm
design membercard :
- there is example how the member-card should look like
the text and logo should be the same as the exemple membercard, the creativity is yours.
- the front side contains text and open space where for writing :
Naam ......
Dansstijlen ......
- the front side contains 12 circels horizontal at the line name at the end of the line "Salsa".
- the front side contains 12 circels horizontal at the line name at the end of the line "Bachata".
- the front side contains 12 circels horizontal at the line name at the end of the line "Kizomba".
- each horizontal line with circels contains a different kind of color/design.
- file format: 7,6 cm x 10,7 cm
Business card :
- there is example how the businesscard should look like
the text and logo should be the same as the exemple buisinesscard, the creativity is yours.
- the design should have a back a front side
File format : 8,7 cm x 5,7 cm

Target Market(s)

Dancing :Salsa, Bachata and Kizomba

Colors

Designer to choose colors to be used in the design.

Requirements
Must have
• same text as seen on the examples.
Nice to have
• see the examples as attachments
Should not have
• - REMOVE TEXT "KOV" from the design
• - REMOVE TEXT "Gratis Parkeren"

```html
<!DOCTYPE html>
<html lang="nl">
<head>
<meta charset="utf-8">
<title>Solera Dance Studio – kaarten</title>
<link href="https://fonts.googleapis.com/css2?family=Raleway:wght@500;600;700;800;900&display=swap" rel="stylesheet">
<style>
  :root {
    --stage-light: #a7a8ac;
    --stage-dark: #3a3b3e;
    --brand-red: #e8302a;
    --pill-red: rgba(236, 56, 40, 0.88);
    --ink: #1c1c1c;
    --paper: #ffffff;
    --rule: #555a60;
  }
  * { margin: 0; padding: 0; box-sizing: border-box; }
  html, body { width: 967px; height: 1200px; overflow: hidden; }
  body {
    position: relative;
    font-family: "Raleway", sans-serif;
    background: linear-gradient(to bottom, var(--stage-light) 0 962px, var(--stage-dark) 962px 100%);
  }
  .card {
    position: absolute;
    left: 73px;
    width: 819px;
    height: 536px;
    overflow: hidden;
    background:
      radial-gradient(ellipse 260px 200px at 20% 18%, rgba(255,255,255,0.95), transparent 70%),
      radial-gradient(ellipse 240px 220px at 62% 62%, rgba(246,190,130,0.55), transparent 70%),
      radial-gradient(ellipse 220px 180px at 95% 55%, rgba(245,200,150,0.55), transparent 70%),
      radial-gradient(ellipse 200px 220px at 3% 55%, rgba(150,190,150,0.45), transparent 70%),
      linear-gradient(160deg, #eef0f0 0%, #e7e9e8 45%, #f0e2d2 100%);
  }
  .card--front { top: 55px; }
  .card--member { top: 609px; }

  .dancers-photo {
    position: absolute;
    left: 40px;
    top: 28px;
    width: 430px;
    height: 510px;
    border-radius: 180px 200px 0 0;
    background:
      radial-gradient(ellipse 120px 160px at 38% 42%, rgba(30,30,36,0.85), transparent 75%),
      radial-gradient(ellipse 150px 190px at 60% 70%, rgba(232,54,40,0.85), transparent 75%),
      linear-gradient(170deg, rgba(60,50,50,0.25), rgba(225,70,50,0.35));
  }

  .brand {
    position: absolute;
    left: 530px;
    width: 266px;
    text-align: center;
    color: var(--ink);
  }
  .card--front .brand { top: 82px; }
  .card--member .brand { top: 86px; }
  .brand__name {
    font-weight: 700;
    font-size: 44px;
    letter-spacing: 6px;
    line-height: 1;
  }
  .brand__studio {
    margin-top: 74px;
    font-weight: 800;
    font-size: 21px;
    letter-spacing: 0.5px;
  }
  .brand__tagline {
    margin-top: 2px;
    font-weight: 500;
    font-size: 6px;
    letter-spacing: 0.3px;
  }

  .styles {
    position: absolute;
    right: 34px;
    top: 300px;
    text-align: right;
    color: var(--brand-red);
    font-weight: 900;
    font-size: 63px;
    line-height: 68px;
  }

  .contact-pill {
    position: absolute;
    left: 0;
    top: 381px;
    width: 365px;
    height: 112px;
    border-radius: 0 56px 56px 0;
    background: var(--pill-red);
    padding: 22px 0 0 60px;
    color: var(--paper);
  }
  .contact-pill__row {
    display: flex;
    align-items: center;
    gap: 6px;
    font-size: 19px;
    font-weight: 600;
    line-height: 24px;
  }
  .contact-pill__icon { width: 19px; height: 19px; flex: none; }

  .member-field {
    position: absolute;
    left: 459px;
    width: 327px;
    display: flex;
    align-items: flex-end;
    color: var(--brand-red);
    font-weight: 700;
    font-size: 17px;
  }
  .member-field__line {
    flex: 1;
    margin: 0 0 3px 3px;
    border-bottom: 1.5px solid var(--rule);
  }
  .member-field--name { top: 271px; }
  .member-field--styles { top: 303px; }

  .stamp {
    position: absolute;
    transform: translate(-50%, -50%);
    border: 2px solid var(--brand-red);
    border-radius: 50%;
    background: var(--paper);
    color: var(--brand-red);
    font-weight: 800;
    display: flex;
    align-items: center;
    justify-content: center;
  }

  .info-band {
    position: absolute;
    left: 0;
    bottom: 0;
    width: 100%;
    height: 52px;
    background: var(--brand-red);
    color: var(--paper);
    font-weight: 700;
    font-size: 21px;
    line-height: 52px;
    padding-left: 43px;
  }
</style>
</head>
<body>

<section class="card card--front">
  <div class="dancers-photo" role="img" aria-label="Foto van een danspaar in zwarte en rode kleding in een dansfiguur"></div>

  <div class="brand">
    <div class="brand__name">SOLERA</div>
    <div class="brand__studio">DANCE STUDIO</div>
    <div class="brand__tagline">FEEL THE RHYTHM, MOVE AS ONE</div>
  </div>

  <h1 class="styles">SALSA<br>BACHATA<br>&amp; KIZOMBA</h1>

  <div class="contact-pill">
    <div class="contact-pill__row">
      <svg class="contact-pill__icon" viewBox="0 0 20 20"><circle cx="10" cy="10" r="8.8" fill="none" stroke="#fff" stroke-width="1.6"/><path d="M7 5.5l1.6 2.3-1 1.2c.7 1.4 1.6 2.3 3 3l1.2-1 2.3 1.6-.9 1.6c-3.5-.3-6.5-3.3-6.8-6.8z" fill="#fff"/></svg>
      <span>0612478350</span>
    </div>
    <div class="contact-pill__row">
      <svg class="contact-pill__icon" viewBox="0 0 20 20"><circle cx="10" cy="10" r="8.8" fill="none" stroke="#fff" stroke-width="1.6"/><rect x="5" y="6.5" width="10" height="7" fill="none" stroke="#fff" stroke-width="1.3"/><path d="M5 6.5l5 4 5-4" fill="none" stroke="#fff" stroke-width="1.3"/></svg>
      <span>soleradenhaag@mailbox.nl</span>
    </div>
    <div class="contact-pill__row">
      <svg class="contact-pill__icon" viewBox="0 0 20 20"><circle cx="10" cy="10" r="8.8" fill="none" stroke="#fff" stroke-width="1.6"/></svg>
      <span>soleradenhaag</span>
    </div>
  </div>
</section>

<section class="card card--member">
  <div class="dancers-photo" role="img" aria-label="Foto van een danspaar in zwarte en rode kleding in een dansfiguur"></div>

  <div class="brand">
    <div class="brand__name">SOLERA</div>
    <div class="brand__studio">DANCE STUDIO</div>
    <div class="brand__tagline">FEEL THE RHYTHM, MOVE AS ONE</div>
  </div>

  <div class="member-field member-field--name">Naam<span class="member-field__line"></span></div>
  <div class="member-field member-field--styles">Dansstijlen<span class="member-field__line"></span></div>

  <div class="stamp" style="left:462px;top:365px;width:60px;height:60px;font-size:30px">1</div>
  <div class="stamp" style="left:526px;top:365px;width:56px;height:56px;font-size:28px">2</div>
  <div class="stamp" style="left:584px;top:365px;width:52px;height:52px;font-size:26px">3</div>
  <div class="stamp" style="left:637px;top:365px;width:48px;height:48px;font-size:25px">4</div>
  <div class="stamp" style="left:686px;top:365px;width:44px;height:44px;font-size:24px">5</div>
  <div class="stamp" style="left:730px;top:365px;width:40px;height:40px;font-size:22px">6</div>
  <div class="stamp" style="left:770px;top:365px;width:36px;height:36px;font-size:21px">7</div>

  <div class="stamp" style="left:462px;top:437px;width:60px;height:60px;font-size:30px">1</div>
  <div class="stamp" style="left:526px;top:437px;width:56px;height:56px;font-size:28px">2</div>
  <div class="stamp" style="left:584px;top:437px;width:52px;height:52px;font-size:26px">3</div>
  <div class="stamp" style="left:637px;top:437px;width:48px;height:48px;font-size:25px">4</div>
  <div class="stamp" style="left:686px;top:437px;width:44px;height:44px;font-size:24px">5</div>
  <div class="stamp" style="left:730px;top:437px;width:40px;height:40px;font-size:22px">6</div>
  <div class="stamp" style="left:770px;top:437px;width:36px;height:36px;font-size:21px">7</div>

  <div class="info-band">Parklaan 24, 2511 AB Den Haag | Fb: Soleradenhaag | Ph:0612478350</div>
</section>

</body>
</html>
```